Mobile Ultrasound Business
Coastal Imaging Partners of Brazos, LLC
Project: Mobile Ultrasound Business
Mobile Ultrasound Business - Health
Creative Brief
Professional
no address (company is mobile)
361-482-9031 (WAVE)
cipbz4@mailvelo.com
www.cipbzllc.com

```html
<!DOCTYPE html>
<html lang="en">
<head>
<meta charset="utf-8">
<title>Coastal Imaging Partners of Brazos, LLC — Business Card</title>
<link rel="stylesheet" href="https://fonts.googleapis.com/css2?family=Cinzel:wght@500;700&display=swap">
<style>
  :root {
    --backdrop: #eef1f4;
    --card-white: #ffffff;
    --brand-blue: #1f5fa8;
    --brand-blue-deep: #164a8a;
    --brand-green: #3aa845;
    --wave-tint: #3f8f7a;
    --text-blue: #2a5d9c;
  }
  * { margin: 0; padding: 0; box-sizing: border-box; }
  html, body {
    width: 1200px;
    height: 799px;
    overflow: hidden;
    background: var(--backdrop);
  }
  .canvas {
    position: relative;
    width: 1200px;
    height: 799px;
  }
  .business-card {
    position: absolute;
    left: 180px;
    top: 160px;
    width: 840px;
    height: 480px;
    background: var(--card-white);
    border-radius: 14px;
    overflow: hidden;
    box-shadow: 0 10px 30px rgba(20, 40, 70, 0.18);
  }
  .side-panel {
    position: absolute;
    inset: 0;
    width: 840px;
    height: 480px;
  }
  .wave-art {
    position: absolute;
    left: 630px;
    top: 20px;
    width: 170px;
    height: 440px;
    border-radius: 50%;
    background: radial-gradient(ellipse at 30% 50%, var(--wave-tint) 0%, var(--brand-blue) 72%);
  }
  .brand-lockup {
    position: absolute;
    left: 44px;
    top: 58px;
    display: flex;
    align-items: center;
    gap: 18px;
  }
  .brand-mark {
    display: flex;
    align-items: center;
    gap: 10px;
  }
  .brand-dot {
    width: 30px;
    height: 30px;
    border-radius: 50%;
    background: var(--brand-green);
  }
  .brand-initials {
    font-family: "Cinzel", serif;
    font-weight: 700;
    font-size: 54px;
    line-height: 1;
    color: var(--brand-blue);
  }
  .brand-name {
    font-family: "Cinzel", serif;
    font-weight: 700;
    font-size: 22px;
    line-height: 1.15;
    color: var(--brand-green);
    max-width: 330px;
  }
  .contact-list {
    position: absolute;
    left: 48px;
    top: 262px;
    list-style: none;
    font-family: "Cinzel", serif;
    font-weight: 500;
    font-size: 18px;
    color: var(--text-blue);
  }
  .contact-item {
    display: flex;
    align-items: center;
    gap: 14px;
    height: 40px;
  }
  .contact-icon {
    width: 20px;
    height: 20px;
    flex: none;
  }
</style>
</head>
<body>
<main class="canvas">
  <article class="business-card">
    <svg class="side-panel" viewBox="0 0 840 480" aria-hidden="true">
      <path d="M612 0 Q540 240 600 480 L840 480 L840 0 Z" fill="var(--brand-blue)"/>
    </svg>
    <div class="wave-art" role="img" aria-label="Decorative sound-wave arcs in green and white"></div>

    <header class="brand-lockup">
      <div class="brand-mark">
        <span class="brand-dot"></span>
        <span class="brand-initials">CIPB</span>
      </div>
      <h1 class="brand-name">Coastal Imaging Partners of Brazos, LLC</h1>
    </header>

    <ul class="contact-list">
      <li class="contact-item">
        <svg class="contact-icon" viewBox="0 0 20 20" aria-hidden="true"><circle cx="10" cy="10" r="10" fill="var(--brand-green)"/><path d="M7 5.5c.6 3.6 3.4 6.9 7.5 8l-1.2 1.6c-4.3-1-7.5-4.6-8.2-8.9z" fill="#fff"/></svg>
        <span>361-482-9031 (WAVE)</span>
      </li>
      <li class="contact-item">
        <svg class="contact-icon" viewBox="0 0 20 20" aria-hidden="true"><circle cx="10" cy="10" r="10" fill="var(--brand-green)"/><path d="M7 5.5c.6 3.6 3.4 6.9 7.5 8l-1.2 1.6c-4.3-1-7.5-4.6-8.2-8.9z" fill="#fff"/></svg>
        <span>361-647-2218</span>
      </li>
      <li class="contact-item">
        <svg class="contact-icon" viewBox="0 0 20 20" aria-hidden="true"><circle cx="10" cy="10" r="10" fill="var(--brand-green)"/><rect x="5" y="6.5" width="10" height="7" fill="none" stroke="#fff" stroke-width="1.4"/><path d="M5 6.5l5 4 5-4" fill="none" stroke="#fff" stroke-width="1.4"/></svg>
        <span>cipbz4@mailvelo.com</span>
      </li>
      <li class="contact-item">
        <svg class="contact-icon" viewBox="0 0 20 20" aria-hidden="true"><circle cx="10" cy="10" r="10" fill="var(--brand-green)"/><circle cx="10" cy="10" r="5" fill="none" stroke="#fff" stroke-width="1.4"/><path d="M5 10h10M10 5c-2.5 3-2.5 7 0 10M10 5c2.5 3 2.5 7 0 10" fill="none" stroke="#fff" stroke-width="1.2"/></svg>
        <span>www.cipbzllc.com</span>
      </li>
    </ul>
  </article>
</main>
</body>
</html>
```